Business Card

We need some ideas for corporate business cards. I'm interested in a double sided card, with one side featuring our corporate logo, the other side with employee information.

Corporate colors, logo etc. available at www.brivalo.com

Industry/Entity Type

Business

Requirements
Must have
• The "Brivalo" logo with stylized "O"

Nice to have
• Preferred font is calibri

```html
<!DOCTYPE html>
<html lang="en">
<head>
<meta charset="utf-8">
<title>Brivalo Business Card</title>
<link href="https://fonts.googleapis.com/css2?family=Carlito:wght@400;700&display=swap" rel="stylesheet">
<style>
  :root {
    --brand-blue: #46608f;
    --brand-blue-deep: #3b5080;
    --band-grey: #cfd1d2;
    --paper-light: #fbfbfb;
    --paper-grey: #d4d5d6;
    --ink: #2b2b2b;
    --url-ink: #41557d;
    --backdrop: #ececec;
  }
  * { margin: 0; padding: 0; box-sizing: border-box; }
  html, body { width: 1200px; height: 874px; overflow: hidden; }
  body {
    background: var(--backdrop);
    font-family: "Carlito", "Calibri", sans-serif;
    position: relative;
  }
  .card {
    position: absolute;
    box-shadow: 0 6px 18px rgba(0,0,0,0.18);
    overflow: hidden;
  }

  /* Front: logo side */
  .card-front {
    left: 170px; top: 190px;
    width: 320px; height: 494px;
    background: linear-gradient(180deg, var(--brand-blue) 0%, var(--brand-blue-deep) 100%);
  }
  .front-logo {
    position: absolute;
    right: 40px; top: 44px;
    writing-mode: vertical-rl;
    transform: rotate(180deg);
    color: #ffffff;
    font-size: 44px;
    font-weight: 400;
    letter-spacing: 3px;
    line-height: 1;
  }
  .front-band {
    position: absolute;
    left: 0; right: 0; bottom: 0;
    height: 74px;
    background: var(--band-grey);
  }
  .band-marker {
    position: absolute;
    left: 50%; top: 0;
    transform: translateX(-50%);
  }
  .front-url {
    position: absolute;
    left: 0; right: 0; top: 24px;
    text-align: center;
    color: var(--url-ink);
    font-size: 17px;
    letter-spacing: 0.5px;
    transform: rotate(180deg);
  }

  /* Back: employee side */
  .card-back {
    left: 570px; top: 270px;
    width: 494px; height: 320px;
    background: linear-gradient(180deg, var(--paper-grey) 0%, var(--paper-light) 100%);
  }
  .back-strip {
    position: absolute;
    left: 0; top: 0; bottom: 0;
    width: 26px;
    background: var(--brand-blue);
  }
  .strip-marker {
    position: absolute;
    left: 26px; top: 150px;
  }
  .contact-block {
    position: absolute;
    left: 262px; top: 36px;
    padding-left: 24px;
    border-left: 2px solid var(--brand-blue);
    height: 122px;
  }
  .person-name {
    color: var(--brand-blue);
    font-weight: 700;
    font-size: 20px;
    line-height: 1.1;
  }
  .person-title {
    color: var(--ink);
    font-weight: 700;
    font-size: 12.5px;
    margin-bottom: 6px;
  }
  .contact-line {
    color: var(--ink);
    font-size: 13.5px;
    line-height: 1.28;
  }
  .contact-line .label {
    color: var(--brand-blue);
    font-weight: 700;
  }
  .address-block {
    position: absolute;
    right: 190px; top: 190px;
    padding-right: 22px;
    border-right: 2px solid var(--brand-blue);
    text-align: right;
    height: 100px;
  }
  .company-name {
    color: var(--brand-blue);
    font-weight: 700;
    font-size: 15px;
  }
  .address-line {
    color: var(--ink);
    font-size: 15px;
    line-height: 1.2;
    white-space: nowrap;
  }
</style>
</head>
<body>
  <section class="card card-front" aria-label="Card front">
    <div class="front-logo">BRIVALO</div>
    <div class="front-band">
      <svg class="band-marker" width="26" height="14" viewBox="0 0 26 14"><polygon points="0,0 26,0 13,14" fill="var(--brand-blue-deep)"/></svg>
      <div class="front-url">www.brivalo.com</div>
    </div>
  </section>

  <section class="card card-back" aria-label="Card back">
    <div class="back-strip"></div>
    <svg class="strip-marker" width="13" height="24" viewBox="0 0 13 24"><polygon points="0,0 13,12 0,24" fill="var(--brand-blue)"/></svg>

    <div class="contact-block">
      <div class="person-name">Clara Novak</div>
      <div class="person-title">Chief Financial Officer</div>
      <div class="contact-line"><span class="label">t:</span> +353 1 555 0140</div>
      <div class="contact-line"><span class="label">f:</span> +353 1 555 0190</div>
      <div class="contact-line"><span class="label">m:</span> +353 1 555 0140</div>
      <div class="contact-line"><span class="label">e:</span> info@brivalo.com</div>
    </div>

    <div class="address-block">
      <div class="company-name">Brivalo</div>
      <div class="address-line">14 Harbour Lane</div>
      <div class="address-line">Meridian Business Park</div>
      <div class="address-line">Dublin 9, Dublin, Ireland</div>
    </div>
  </section>
</body>
</html>
```